New Web 2.0 responsive website for popup advertisement network

We need a responsive web design for a new popup advertisement network company Clikvantra.com based in Newport Beach, California.

We need the design for the main site as well as the interface design for the member portal login area.

Below is the requirement and concept for the website / portal. 

1. With reference to http://tabrivex.com/  (Overall  home layout design and menu bar can follow this website (except the homepage banner section) ,color theme change to #81D8D0)

2. Integrate 3 step process in the homepage for easy reference. Follow the concept in the website below but use better graphic and images to present. Can integrate this in homepage banner section.
   reference:  http://quorlent.net/, http://zandimex.com/ 

3.  Use the nice look ad tag line in the homepage banner section as well. Can refer to the site below.
     http://www.yieldbarrow.com/#publishers
 
4. Sign up button must be clear and obvious in the homepage.

We required the design for the pages below.
1. Homepage
2. Dashboard
3. Add Website
3. Code Generator
4. Website
5. Report

(Please refer to the attached image for the concept and field required in the page)

Target Market(s)

US, web owner such as blogger or content sites

Industry/Entity Type

Advertising

Logo Text

Scientific and Fun

Coding

Coded - Design and coding required

Number of Pages Required

5+ page

Font styles to use
Sans Serif

Colors
0692cd

```html
<!DOCTYPE html>
<html lang="en">
<head>
<meta charset="utf-8">
<title>Clikvantra – Premium Ad Network</title>
<link href="https://fonts.googleapis.com/css2?family=Ubuntu:wght@400;500;700&family=Open+Sans:wght@400;600;700&display=swap" rel="stylesheet">
<style>
:root{
  --brand:#1a6fb5;
  --blue:#1a93d3;
  --blue-dark:#1d5ea8;
  --teal:#74cfc6;
  --ink:#222;
  --body:#666;
  --line:#e3e3e3;
  --soft:#f3f3f3;
  --white:#fff;
}
*{margin:0;padding:0;box-sizing:border-box}
html,body{width:1200px;height:2503px;overflow:hidden}
body{position:relative;font-family:"Open Sans",Arial,sans-serif;color:var(--body);background:var(--white)}
h1,h2,h3,h4{font-weight:400}
.abs{position:absolute}
.center{text-align:center}

/* header */
.site-header{left:0;top:0;width:1200px;height:112px;background:var(--white)}
.brand{left:98px;top:38px;font-family:"Ubuntu",sans-serif;font-weight:700;font-size:32px;color:var(--brand);letter-spacing:1px}
.nav-link{top:49px;font-size:13px;color:#444;text-decoration:none;letter-spacing:.5px;font-family:"Ubuntu",sans-serif;white-space:nowrap}
.btn-register{left:1011px;top:42px;width:90px;height:33px;background:var(--brand);color:var(--white);font-size:13px;font-weight:700;font-family:"Ubuntu",sans-serif;display:flex;align-items:center;justify-content:center;border-radius:2px}

/* hero */
.hero{left:0;top:112px;width:1200px;height:551px;background:linear-gradient(135deg,#7fd6cd 0%,#6cc7be 45%,#5fb5ae 100%)}
.hero-photo{left:0;top:0;width:1200px;height:551px;background:radial-gradient(ellipse at 70% 40%,rgba(40,90,100,.25),rgba(0,0,0,0) 60%)}
.hero-title{left:0;top:78px;width:1200px;font-family:"Ubuntu",sans-serif;font-weight:700;font-size:37px;color:var(--white);letter-spacing:.5px}
.hero-text{left:0;top:140px;width:1200px;font-size:14.5px;line-height:23px;color:rgba(255,255,255,.92)}
.step{width:206px;height:206px;border:3px solid rgba(255,255,255,.75);border-radius:50%;top:252px}
.step-icon{position:absolute;left:0;top:42px;width:100%;display:flex;justify-content:center}
.step-rule{position:absolute;left:0;top:110px;width:100%;height:1px;background:rgba(255,255,255,.45)}
.step-label{position:absolute;left:0;top:128px;width:100%;text-align:center;color:var(--white);font-size:14px;line-height:22px;font-family:"Ubuntu",sans-serif;letter-spacing:.5px}
.arrow{top:418px}

/* signup band */
.signup-band{left:0;top:663px;width:1200px;height:106px;background:linear-gradient(#fbfbfb,#ececec)}
.signup-title{left:97px;top:17px;font-family:"Ubuntu",sans-serif;font-size:27px;color:var(--ink)}
.signup-text{left:97px;top:58px;font-size:14px;color:#444}
.btn-signup{left:876px;top:31px;width:225px;height:42px;background:var(--blue);color:var(--white);font-size:15px;display:flex;align-items:center;justify-content:center;gap:8px;border-radius:2px}

/* welcome */
.welcome-title{left:0;top:804px;width:1200px;font-family:"Ubuntu",sans-serif;font-size:38px;color:var(--ink)}
.welcome-text{left:160px;top:861px;width:880px;font-size:12px;line-height:20px;color:#444}
.card{top:936px;width:487px;height:327px;border:1px solid var(--line)}
.card-alt{background:#f6f6f6}
.card-icon{position:absolute;left:193px;top:20px;width:100px;height:100px;border:2px solid var(--blue);border-radius:50%;display:flex;align-items:center;justify-content:center}
.card-title{position:absolute;left:0;top:130px;width:100%;text-align:center;font-family:"Ubuntu",sans-serif;font-size:21px;color:#444}
.card-text{position:absolute;left:30px;top:169px;width:425px;text-align:center;font-size:11.5px;line-height:21px;color:#555}
.btn-outline{position:absolute;left:186px;top:266px;width:113px;height:34px;border:1.5px solid var(--blue);border-radius:3px;color:#555;font-size:15px;display:flex;align-items:center;justify-content:center;background:var(--white)}

/* features */
.features{left:0;top:1312px;width:1200px;height:412px;background:linear-gradient(90deg,#1c92d2,#1b8ccd)}
.features-photo{left:720px;top:0;width:480px;height:412px;background:linear-gradient(180deg,rgba(20,80,130,.18),rgba(20,80,130,.05))}
.features-title{left:0;top:44px;width:1200px;font-family:"Ubuntu",sans-serif;font-size:31px;color:var(--white)}
.feature{width:340px;height:100px}
.feature-icon{position:absolute;left:0;top:0;width:74px;height:74px;border:3px solid var(--white);border-radius:50%;display:flex;align-items:center;justify-content:center}
.feature-title{position:absolute;left:90px;top:-4px;font-family:"Ubuntu",sans-serif;font-size:18px;color:var(--white);white-space:nowrap}
.feature-text{position:absolute;left:90px;top:28px;width:220px;font-size:11px;line-height:21px;color:rgba(255,255,255,.92)}

/* insights */
.insights{left:0;top:1724px;width:1200px;height:462px;background:linear-gradient(#fff 70%,#f3f5f7)}
.insights-kicker{left:110px;top:82px;font-family:"Ubuntu",sans-serif;font-size:32px;color:var(--ink)}
.insights-title{left:110px;top:117px;font-family:"Ubuntu",sans-serif;font-size:53px;color:var(--blue)}
.insights-text{left:110px;top:185px;width:480px;font-size:12px;line-height:20px;color:#333}
.insights-list{left:110px;top:242px;list-style:none}
.insights-list li{font-size:12.5px;color:#444;height:25.5px;display:flex;align-items:center;gap:12px;letter-spacing:.3px}
.btn-learn{left:110px;top:362px;width:180px;height:40px;background:var(--blue);color:var(--white);font-size:15px;display:flex;align-items:center;border-radius:2px;overflow:hidden}
.btn-learn span{padding-left:15px;flex:1}
.btn-learn i{width:44px;height:40px;background:#1682bd;display:flex;align-items:center;justify-content:center;clip-path:polygon(22% 0,100% 0,100% 100%,0 100%)}
.insights-photo{left:609px;top:28px;width:492px;height:434px;background:linear-gradient(180deg,#f5f5f5 0%,#d9dde2 55%,#3a3d44 100%)}

/* footer */
.site-footer{left:0;top:2186px;width:1200px;height:254px;background:var(--soft)}
.footer-head{font-family:"Ubuntu",sans-serif;font-size:16px;color:#333;top:38px;letter-spacing:.3px}
.footer-text{font-size:11.5px;line-height:20px;color:#444}
.field{left:98px;width:261px;height:42px;background:var(--white);border:1px solid #e2e2e2;font-size:11.5px;color:#333;padding-left:12px;display:flex;align-items:center}
.btn-subscribe{left:262px;top:176px;width:97px;height:42px;background:var(--brand);color:var(--white);font-size:12.5px;display:flex;align-items:center;justify-content:center}
.quote{left:482px;top:74px;width:360px;font-size:11.5px;line-height:21px;font-style:italic;color:#444}
.quote-name{left:482px;top:153px;font-size:13px;color:#333;font-family:"Ubuntu",sans-serif}
.quote-role{left:482px;top:178px;font-size:10.5px;color:#333}
.contact-row{left:911px;display:flex;align-items:center;gap:14px;font-size:12.5px;color:#333}
.social{left:911px;top:186px;display:flex;gap:9px}
.social span{width:28px;height:28px;display:block}

.legal-bar{left:0;top:2440px;width:1200px;height:63px;background:var(--blue-dark);display:flex;align-items:center;justify-content:center;color:rgba(255,255,255,.9);font-size:11.5px}
.legal-bar b{font-weight:700;margin:0 3px}
</style>
</head>
<body>

<header class="site-header abs">
  <div class="brand abs">CLIKVANTRA</div>
  <nav>
    <a class="nav-link abs" style="left:497px">HOME</a>
    <a class="nav-link abs" style="left:577px">PUBLISHERS</a>
    <a class="nav-link abs" style="left:697px">ADVERTISERS</a>
    <a class="nav-link abs" style="left:820px">REGULATION</a>
    <a class="nav-link abs" style="left:941px">BLOG</a>
  </nav>
  <div class="btn-register abs">REGISTER</div>
</header>

<section class="hero abs">
  <div class="hero-photo abs" role="img" aria-label="Photo of a business team at work, washed in teal"></div>
  <h1 class="hero-title abs center">PREMIUM CLIKVANTRA AD NETWORK</h1>
  <p class="hero-text abs center">Lorem ipsum dolor sit amet, consectetur adipiscing elit, sed do eiusmod tempor incididunt ut labore et dolore magna aliqua.<br>Ut enim ad minim veniam, quis nostrud exercitation ullamco laboris nisi ut aliquip ex ea commodo consequat.</p>

  <div class="step abs" style="left:199px">
    <div class="step-icon"><svg width="64" height="56" viewBox="0 0 64 56"><path d="M2 26 L62 2 L48 54 L30 38 Z" fill="none" stroke="#fff" stroke-width="4" stroke-linejoin="round"/><path d="M30 38 L62 2 M30 38 L28 52 L38 44" fill="none" stroke="#fff" stroke-width="4" stroke-linejoin="round"/></svg></div>
    <div class="step-rule"></div>
    <div class="step-label">SET UP</div>
  </div>
  <div class="step abs" style="left:493px">
    <div class="step-icon"><svg width="44" height="62" viewBox="0 0 44 62"><path d="M22 3 A19 19 0 0 1 34 37 L32 44 H12 L10 37 A19 19 0 0 1 22 3 Z" fill="none" stroke="#fff" stroke-width="4"/><path d="M13 50 H31 M15 56 H29" stroke="#fff" stroke-width="4" stroke-linecap="round"/></svg></div>
    <div class="step-rule"></div>
    <div class="step-label">SHOW<br>RELEVANT ADS</div>
  </div>
  <div class="step abs" style="left:793px">
    <div class="step-icon"><svg width="40" height="62" viewBox="0 0 40 62"><path d="M33 17 C30 10 8 8 8 20 C8 32 33 28 33 41 C33 53 10 53 6 45" fill="none" stroke="#fff" stroke-width="6" stroke-linecap="round"/><path d="M20 2 V60" stroke="#fff" stroke-width="5"/></svg></div>
    <div class="step-rule"></div>
    <div class="step-label">EARN MONEY</div>
  </div>

  <svg class="arrow abs" style="left:398px" width="104" height="52" viewBox="0 0 104 52"><path d="M2 40 C30 54 70 48 94 12" fill="none" stroke="#fff" stroke-width="5" stroke-linecap="round"/><path d="M78 12 L97 6 L96 26" fill="none" stroke="#fff" stroke-width="5" stroke-linecap="round" stroke-linejoin="round"/></svg>
  <svg class="arrow abs" style="left:699px" width="104" height="52" viewBox="0 0 104 52"><path d="M2 40 C30 54 70 48 94 12" fill="none" stroke="#fff" stroke-width="5" stroke-linecap="round"/><path d="M78 12 L97 6 L96 26" fill="none" stroke="#fff" stroke-width="5" stroke-linecap="round" stroke-linejoin="round"/></svg>
</section>

<section class="signup-band abs">
  <h2 class="signup-title abs">Do you have a website?</h2>
  <p class="signup-text abs">Clikvantra will maximize your advertising revenue with cutting-edge clikvantra technology.</p>
  <div class="btn-signup abs">
    <svg width="14" height="16" viewBox="0 0 14 16"><rect x="1" y="7" width="12" height="9" rx="1" fill="#fff"/><path d="M4 7 V4 A3 3 0 0 1 10 4" fill="none" stroke="#fff" stroke-width="2"/></svg>
    Sign Up For An Account
  </div>
</section>

<h2 class="welcome-title abs center">Welcome To Clikvantra</h2>
<p class="welcome-text abs center">Lorem ipsum dolor sit amet, consectetur adipiscing elit, sed do eiusmod tempor incididunt ut labore et dolore magna aliqua. Ut enim ad minim veniam, quis nostrud exercitation ullamco laboris nisi ut aliquip ex ea commodo consequat. Duis aute irure dolor in reprehenderit in voluptate</p>

<article class="card card-alt abs" style="left:98px">
  <div class="card-icon"><svg width="54" height="44" viewBox="0 0 54 44"><path d="M4 14 H16 L40 3 V39 L16 28 H4 Z" fill="var(--blue)"/><path d="M12 28 L18 42 H24 L20 28" fill="var(--blue)"/><path d="M46 14 Q52 21 46 28" fill="none" stroke="var(--blue)" stroke-width="4" stroke-linecap="round"/></svg></div>
  <h3 class="card-title">Advertisers</h3>
  <p class="card-text">Lorem ipsum dolor sit amet, consectetur adipiscing elit, sed do eiusmod tempor incididunt ut labore et dolore magna aliqua. Ut enim ad minim veniam, quis nostrud exercitation ullamco laboris nisi ut aliquip ex ea commodo consequat. Duis aute irure dolor in reprehenderit in voluptate</p>
  <div class="btn-outline">Read More</div>
</article>
<article class="card abs" style="left:584px">
  <div class="card-icon"><svg width="44" height="46" viewBox="0 0 44 46"><circle cx="22" cy="12" r="11" fill="var(--blue)"/><path d="M2 46 V38 A14 14 0 0 1 16 24 H28 A14 14 0 0 1 42 38 V46 Z" fill="var(--blue)"/></svg></div>
  <h3 class="card-title">Publishers</h3>
  <p class="card-text">Lorem ipsum dolor sit amet, consectetur adipiscing elit, sed do eiusmod tempor incididunt ut labore et dolore magna aliqua. Ut enim ad minim veniam, quis nostrud exercitation ullamco laboris nisi ut aliquip ex ea commodo consequat. Duis aute irure dolor in reprehenderit in voluptate</p>
  <div class="btn-outline">Read More</div>
</article>

<section class="features abs">
  <div class="features-photo abs" role="img" aria-label="Faint photo of a businessman on the phone over a city skyline"></div>
  <h2 class="features-title abs center">Clikvantra Service Features</h2>

  <div class="feature abs" style="left:98px;top:125px">
    <div class="feature-icon"><svg width="34" height="34" viewBox="0 0 34 34"><circle cx="17" cy="17" r="14" fill="none" stroke="#fff" stroke-width="3"/><path d="M17 9 V18 H24" fill="none" stroke="#fff" stroke-width="3"/></svg></div>
    <h3 class="feature-title">Realtime bidding system</h3>
    <p class="feature-text">Lorem ipsum dolor sit amet, coetur adipiscing elit. Vivamus luctus urna sed urna ultricies ac tempor</p>
  </div>
  <div class="feature abs" style="left:452px;top:125px">
    <div class="feature-icon"><svg width="30" height="34" viewBox="0 0 30 34"><rect x="3" y="15" width="24" height="18" rx="2" fill="#fff"/><path d="M8 15 V9 A7 7 0 0 1 22 7" fill="none" stroke="#fff" stroke-width="3"/><rect x="13" y="20" width="4" height="8" fill="var(--blue)"/></svg></div>
    <h3 class="feature-title">Dedicated account manager</h3>
    <p class="feature-text">Lorem ipsum dolor sit amet, coetur adipiscing elit. Vivamus luctus urna sed urna ultricies ac tempor</p>
  </div>
  <div class="feature abs" style="left:809px;top:125px">
    <div class="feature-icon"><svg width="34" height="26" viewBox="0 0 34 26"><rect x="2" y="2" width="30" height="22" rx="2" fill="none" stroke="#fff" stroke-width="3"/><path d="M2 4 L17 15 L32 4" fill="none" stroke="#fff" stroke-width="3"/></svg></div>
    <h3 class="feature-title">24/7 support</h3>
    <p class="feature-text">Lorem ipsum dolor sit amet, coetur adipiscing elit. Vivamus luctus urna sed urna ultricies ac tempor</p>
  </div>

  <div class="feature abs" style="left:98px;top:262px">
    <div class="feature-icon"><svg width="32" height="30" viewBox="0 0 32 30"><path d="M2 2 V28 H30" fill="none" stroke="#fff" stroke-width="3"/><rect x="8" y="14" width="4" height="11" fill="#fff"/><rect x="14" y="8" width="4" height="17" fill="#fff"/><rect x="20" y="12" width="4" height="13" fill="#fff"/><rect x="26" y="6" width="3" height="19" fill="#fff"/></svg></div>
    <h3 class="feature-title">Realtime reports</h3>
    <p class="feature-text">Lorem ipsum dolor sit amet, coetur adipiscing elit. Vivamus luctus urna sed urna ultricies ac tempor</p>
  </div>
  <div class="feature abs" style="left:452px;top:262px">
    <div class="feature-icon"><svg width="32" height="32" viewBox="0 0 32 32"><path d="M8 16 L24 7 M8 16 L24 25" stroke="#fff" stroke-width="3"/><circle cx="7" cy="16" r="5" fill="#fff"/><circle cx="25" cy="6" r="5" fill="#fff"/><circle cx="25" cy="26" r="5" fill="#fff"/></svg></div>
    <h3 class="feature-title">Instant deposits</h3>
    <p class="feature-text">Lorem ipsum dolor sit amet, coetur adipiscing elit. Vivamus luctus urna sed urna ultricies ac tempor</p>
  </div>
  <div class="feature abs" style="left:809px;top:262px">
    <div class="feature-icon"><svg width="32" height="32" viewBox="0 0 32 32"><path d="M4 28 L18 14" stroke="#fff" stroke-width="5" stroke-linecap="round"/><path d="M16 12 A8 8 0 0 1 28 4 L23 10 L26 13 L30 8 A8 8 0 0 1 20 18 Z" fill="#fff"/></svg></div>
    <h3 class="feature-title">Full control</h3>
    <p class="feature-text">Lorem ipsum dolor sit amet, coetur adipiscing elit. Vivamus luctus urna sed urna ultricies ac tempor</p>
  </div>
</section>

<section class="insights abs">
  <div class="insights-kicker abs">CLIKVANTRA</div>
  <h2 class="insights-title abs">Network insights</h2>
  <p class="insights-text abs">Lorem ipsum dolor sit amet, consectetur adipiscing elit, sed do eiusmod tempor incididunt ut labore et dolore magna aliqua. Ut enim ad minim veniam,</p>
  <ul class="insights-list abs">
    <li><svg width="13" height="11" viewBox="0 0 13 11"><path d="M1 6 L5 10 L12 1" fill="none" stroke="var(--brand)" stroke-width="2.5"/></svg>WEBSITES</li>
    <li><svg width="13" height="11" viewBox="0 0 13 11"><path d="M1 6 L5 10 L12 1" fill="none" stroke="var(--brand)" stroke-width="2.5"/></svg>AD CAMPAIGNS</li>
    <li><svg width="13" height="11" viewBox="0 0 13 11"><path d="M1 6 L5 10 L12 1" fill="none" stroke="var(--brand)" stroke-width="2.5"/></svg>POP-UNDERS TODAY</li>
    <li><svg width="13" height="11" viewBox="0 0 13 11"><path d="M1 6 L5 10 L12 1" fill="none" stroke="var(--brand)" stroke-width="2.5"/></svg>TOP NETWORK BID</li>
  </ul>
  <div class="btn-learn abs"><span>LEARN MORE</span><i><svg width="16" height="14" viewBox="0 0 16 14"><path d="M1 7 H13 M8 2 L13 7 L8 12" fill="none" stroke="#fff" stroke-width="2.5"/></svg></i></div>
  <div class="insights-photo abs" role="img" aria-label="Photo of two businessmen in suits shaking hands"></div>
</section>

<footer class="site-footer abs">
  <h4 class="footer-head abs" style="left:98px">SIGN UP FOR NEWSLETTER</h4>
  <p class="footer-text abs" style="left:98px;top:70px;width:265px">Excepteur sint occaecat cupidatat non proident, sunt in culpa qui officia deserunt</p>
  <div class="field abs" style="top:124px">Enter Name</div>
  <div class="field abs" style="top:176px">Enter Email</div>
  <div class="btn-subscribe abs">SUBSCRIBE</div>

  <h4 class="footer-head abs" style="left:482px">TESTIMONIALS</h4>
  <p class="quote abs">" Sed ut perspiciatis unde omnis iste natus error sit voluptatem accusantium doloremque laudantium, totam rem aperiam, eaque ipsa quae ab illo inventore veritatis et quasi archite"</p>
  <div class="quote-name abs">CLIKVANTRA</div>
  <div class="quote-role abs">Dana Hollis,City Name</div>

  <h4 class="footer-head abs" style="left:911px">CONTACT US</h4>
  <p class="footer-text abs" style="left:911px;top:70px;font-size:12.5px">Clikvantra<br>PO BOX TBA, Harlowmere</p>
  <div class="contact-row abs" style="top:124px"><svg width="16" height="16" viewBox="0 0 16 16"><path d="M3 1 L6 4 L4 7 Q6 10 9 12 L12 10 L15 13 L12 15 Q2 12 1 4 Z" fill="none" stroke="#777" stroke-width="1.3"/></svg>+1 800 5550 147</div>
  <div class="contact-row abs" style="top:150px"><svg width="16" height="12" viewBox="0 0 16 12"><rect x="1" y="1" width="14" height="10" fill="none" stroke="#777" stroke-width="1.3"/><path d="M1 1 L8 7 L15 1" fill="none" stroke="#777" stroke-width="1.3"/></svg>info@clikvantra.com</div>
  <div class="social abs">
    <span style="background:#d6452f"></span>
    <span style="background:#345a9b"></span>
    <span style="background:#23a6e0"></span>
    <span style="background:#0e7bb6"></span>
    <span style="background:#d3302b"></span>
  </div>
</footer>

<div class="legal-bar abs">©2014 - 2015 <b>CLIKVANTRA</b>.. All Rights Reserved.</div>

</body>
</html>
```